New Zealand Luggage Importer Needs Business Cards

We need professional, creative and fashionable business cards created.
We are based in New Zealand and import and distribute high-end, quality, fashionable and durable luggage.
We pride ourselves on selling the very best quality luggage, second only to 1 brand (which we won't mention here)...we use the same manufacturer. However, our prices are much more reasonable.
Business
Sam Ortiz
027 481 2956
3/17 Kestrel Lane, Morrow Flats, Auckland, 0614
PO Box 208354, North Shore, Auckland 0792
09-527-3061
sales@brindlecases.co.nz / www.brindlecases.co.nz

```html
<!DOCTYPE html>
<html lang="en">
<head>
<meta charset="utf-8">
<title>Brindle Cases – Business Card</title>
<link href="https://fonts.googleapis.com/css2?family=Michroma&family=Lato:wght@400;700;900&display=swap" rel="stylesheet">
<style>
  :root {
    --page-bg: #1c1b19;
    --card-light: #8d8c88;
    --card-mid: #7b7a76;
    --card-dark: #66655f;
    --panel: #1f1f1e;
    --gold-light: #e0c36a;
    --gold: #c9a347;
    --gold-deep: #9c7a2a;
    --ink: #121212;
    --ink-soft: #2a2a28;
    --text-light: #f2f0ea;
  }
  html, body {
    margin: 0;
    padding: 0;
    width: 1200px;
    height: 735px;
    overflow: hidden;
    background: var(--page-bg);
  }
  .canvas {
    position: relative;
    width: 1200px;
    height: 735px;
  }
  .card {
    position: absolute;
    left: 150px;
    top: 110px;
    width: 900px;
    height: 514px;
    border-radius: 26px;
    overflow: hidden;
    background: radial-gradient(ellipse at 35% 30%, var(--card-light) 0%, var(--card-mid) 55%, var(--card-dark) 100%);
  }
  .card-surface {
    position: absolute;
    inset: 0;
  }
  .card-shapes {
    position: absolute;
    inset: 0;
    width: 900px;
    height: 514px;
  }
  .brand-name {
    position: absolute;
    left: 56px;
    top: 52px;
    margin: 0;
    font-family: "Michroma", sans-serif;
    font-weight: 400;
    font-size: 44px;
    letter-spacing: 1px;
    color: var(--ink);
    white-space: nowrap;
  }
  .person {
    position: absolute;
    left: 92px;
    top: 196px;
  }
  .person-name {
    margin: 0 0 0 22px;
    font-family: "Michroma", sans-serif;
    font-size: 38px;
    font-weight: 400;
    letter-spacing: 1px;
    color: var(--gold);
    background: linear-gradient(180deg, var(--gold-light) 0%, var(--gold) 55%, var(--gold-deep) 100%);
    -webkit-background-clip: text;
    background-clip: text;
    -webkit-text-fill-color: transparent;
    line-height: 1.1;
    white-space: nowrap;
  }
  .person-role {
    margin: -4px 0 0 0;
    font-family: "Lato", sans-serif;
    font-weight: 900;
    font-size: 15px;
    letter-spacing: 1px;
    color: var(--ink-soft);
  }
  .contact-list {
    position: absolute;
    right: 40px;
    top: 252px;
    margin: 0;
    padding: 0;
    list-style: none;
    font-family: "Lato", sans-serif;
    font-size: 20px;
    letter-spacing: 1px;
    color: var(--text-light);
  }
  .contact-item {
    display: flex;
    justify-content: flex-end;
    align-items: center;
    height: 32px;
  }
  .contact-icon {
    width: 18px;
    height: 18px;
    margin-left: 16px;
    flex: none;
  }
  .address-line {
    position: absolute;
    left: 40px;
    right: 40px;
    bottom: 52px;
    margin: 0;
    font-family: "Lato", sans-serif;
    font-size: 17px;
    letter-spacing: 0.6px;
    color: var(--text-light);
    white-space: nowrap;
  }
  .address-sep {
    margin: 0 8px;
  }
</style>
</head>
<body>
<main class="canvas">
  <article class="card">
    <div class="card-surface" role="img" aria-label="Smoky grey stone texture across the card face"></div>

    <svg class="card-shapes" viewBox="0 0 900 514" aria-hidden="true">
      <defs>
        <linearGradient id="goldBand" x1="0" y1="0" x2="1" y2="0">
          <stop offset="0" stop-color="#b8923a"/>
          <stop offset="0.45" stop-color="#e6cb78"/>
          <stop offset="1" stop-color="#a9852f"/>
        </linearGradient>
      </defs>
      <path class="gold-band" d="M0,314 L572,314 L548,358 L0,358 Z" fill="url(#goldBand)"/>
      <path class="contact-panel" d="M0,356 L548,356 Q562,356 570,342 L622,250 Q634,230 658,230 L900,230 L900,514 L0,514 Z" fill="var(--panel)" fill-opacity="0.94"/>
    </svg>

    <h1 class="brand-name">BRINDLE CASES</h1>

    <div class="person">
      <h2 class="person-name">SAM ORTIZ</h2>
      <p class="person-role">FOUNDER</p>
    </div>

    <ul class="contact-list">
      <li class="contact-item">027 481 2956
        <svg class="contact-icon" viewBox="0 0 18 18" aria-hidden="true"><rect x="5" y="1" width="8" height="16" rx="1.5" fill="var(--gold)"/><rect x="6.5" y="3" width="5" height="9" fill="var(--panel)"/></svg>
      </li>
      <li class="contact-item">09-527-3061
        <svg class="contact-icon" viewBox="0 0 18 18" aria-hidden="true"><path d="M4 2 L7 2 L8 6 L6 7.5 Q7.5 10.5 10.5 12 L12 10 L16 11 L16 14 Q16 16 14 16 Q3 15 2 4 Q2 2 4 2 Z" fill="var(--gold)"/></svg>
      </li>
      <li class="contact-item">sales@brindlecases.co.nz
        <svg class="contact-icon" viewBox="0 0 18 18" aria-hidden="true"><rect x="1.5" y="4" width="15" height="10" fill="var(--gold)"/><path d="M1.5 4 L9 10 L16.5 4" fill="none" stroke="var(--panel)" stroke-width="1.3"/></svg>
      </li>
      <li class="contact-item">www.brindlecases.co.nz
        <svg class="contact-icon" viewBox="0 0 18 18" aria-hidden="true"><circle cx="9" cy="9" r="7.5" fill="var(--gold)"/><ellipse cx="9" cy="9" rx="3" ry="7.5" fill="none" stroke="var(--panel)" stroke-width="1.1"/><path d="M1.5 9 H16.5 M3 5 H15 M3 13 H15" stroke="var(--panel)" stroke-width="1.1"/></svg>
      </li>
    </ul>

    <p class="address-line">3/17 Kestrel Lane, Morrow Flats, Auckland, 0614<span class="address-sep">|</span>PO Box 208354, North Shore, Auckland 0792</p>
  </article>
</main>
</body>
</html>
```